Industrial Inspection & Testing Company Needs Brochure

We need a brochure design for a company based in Western Pennsylvania, USA. Our company performs services mainly in industrial sites. These can include manufacturing, health & medical, power generation, and more. We use infrared thermography, vibration analysis, ultrasonic thickness testing, dynamic balancing and other practices to provide predictive maintenance to our customers. Please see our website for a more thorough explanation of our services. www.kortalinspect.com

Complete list of services:

Infrared Thermal Imaging
Vibration Analysis
High Temperature Video & Photography
High Speed Video
Laser Alignment
Dynamic Balancing
Motor Meggering
Leak Detection
Ultrasonic Thickness Testing
Oil Analysis

KRT, LLC - P.O. Box 4738 - Maple Hollow, PA 15842
Phone: 555-318-4471 / Fax: 555-318-4479

MISSION

KRT, LLC will provide the highest quality, cost effective, world class PdM services in the industry. Our commitment to continuing education and growth will afford our engineers the tools needed to stay on the cutting edge of technology. We believe in the implementation of Predictive Maintenance services to increase overall equipment reliability, reduce costs and improve profitability. Our goal is to provide continuous improvements to these processes. The company will network with various industry professionals to offer the widest range of equipment, training and reliability services available. Meeting these goals will ensure the company’s longevity and allow our valued customers to achieve the cost reduction goals that are needed in today’s competitive marketplace.
HISTORY
KRT, LLC was founded in March 1984, which emerged from the Granite Forge Industries’ Laboratory Campus, Monroeville, Pennsylvania. Its founders headed the Thermography and Photoinstrumentation Department of that facility.
While at the G. F. Industries Laboratory Campus, they established the utilization of thermography as a valuable tool for evaluating equipment and facilities in the steel industry. Their work set the standards for the use of thermography in the steel industry that continues today with KRT. Although the original thermographic equipment was crude, bulky and slow, KRT has maintained its position as an industry leader. Today KRT uses the most technologically advanced infrared systems available for on-site nondestructive industrial inspections.
In addition, while at G. F. Industries Laboratory, the founders of KRT pioneered the use of photographic cameras and high-speed motion pictures as another form of a predictive and preventative maintenance tool. Specially constructed camera systems with thermal protective housings were developed for inspecting blast furnace interior stockline armor areas, stove domes, and other high-temperature areas.
Today KRT remains on the cutting-edge in providing a wide range of nondestructive inspection services to industry.

***All of the photos and documents attached were either shot by us or purchased stock photos***

I realize that only a few images might be used, I just wanted to upload many to give designers a broad range to choose from.

Target Market(s)

Large industrial customers who use large amounts of electricity, heavy duty machinery, or both.

Industry/Entity Type

Industrial

Requirements
Must have
• Need a 3 full page tri-fold design (not skinny column tri-fold)

Contact information for our company, list of our services, our logo (possible redesign of logo), photos from our inspections that will be attached.
Nice to have
• List of services, breif explanation of each with graphical representation, contact information

```html
<!DOCTYPE html>
<html lang="en">
<head>
<meta charset="utf-8">
<title>KRT, LLC – Services Brochure</title>
<link rel="stylesheet" href="https://fonts.googleapis.com/css2?family=Arimo:wght@400;700&display=swap">
<style>
  :root {
    --orange: #f0791f;
    --orange-deep: #e0601a;
    --accent: #f7a234;
    --ink: #111111;
    --panel-dark: #1c1c1c;
    --band-grey: #6a6a6a;
    --text-light: #f2f2f2;
    --text-muted: #d8d8d8;
    --divider: #ffffff;
  }
  html, body {
    margin: 0;
    padding: 0;
    width: 1200px;
    height: 915px;
    overflow: hidden;
    background: #ffffff;
    font-family: "Arimo", Arial, sans-serif;
  }
  .brochure {
    position: relative;
    width: 1200px;
    height: 915px;
    overflow: hidden;
    background: var(--panel-dark);
  }
  .shapes { position: absolute; inset: 0; }
  .block {
    position: absolute;
    color: var(--text-light);
    font-size: 13.2px;
    line-height: 16px;
  }
  .block p { margin: 0; }
  .ln { display: block; white-space: nowrap; }
  .just { text-align: justify; text-align-last: justify; }
  .heading {
    color: var(--accent);
    font-size: 14.2px;
    line-height: 16px;
    text-transform: uppercase;
    margin: 0;
    font-weight: 400;
    white-space: nowrap;
  }
  .mission-title {
    position: absolute;
    left: 38px;
    top: 34px;
    color: #fff;
    font-size: 25px;
    line-height: 30px;
    margin: 0;
    font-weight: 400;
  }
  .mission-text { left: 33px; top: 87px; font-size: 12.9px; }
  .services-title {
    position: absolute;
    left: 355px;
    top: 213px;
    margin: 0;
    color: #fff;
    font-size: 24px;
    line-height: 28px;
    font-weight: 400;
  }
  .list-title {
    position: absolute;
    left: 29px;
    top: 687px;
    margin: 0;
    color: #fff;
    font-size: 16px;
    line-height: 21px;
    font-weight: 400;
  }
  .service-list {
    position: absolute;
    left: 34px;
    top: 715px;
    margin: 0;
    padding: 0;
    list-style: none;
    color: var(--text-muted);
    font-size: 12px;
    line-height: 18.8px;
  }
  .service-list li::before {
    content: "";
    display: inline-block;
    width: 4px;
    height: 4px;
    background: var(--accent);
    margin-right: 4px;
    vertical-align: middle;
  }
</style>
</head>
<body>
<main class="brochure">
  <svg class="shapes" width="1200" height="915" viewBox="0 0 1200 915">
    <defs>
      <linearGradient id="middleGrad" x1="0" y1="0" x2="1" y2="1">
        <stop offset="0" stop-color="#3e3e3e"/>
        <stop offset="0.5" stop-color="#141414"/>
        <stop offset="1" stop-color="#4a4a4a"/>
      </linearGradient>
      <linearGradient id="rightGrad" x1="0" y1="0" x2="1" y2="0">
        <stop offset="0" stop-color="#2a2a2a"/>
        <stop offset="1" stop-color="#4b4b4b"/>
      </linearGradient>
      <linearGradient id="leftGrad" x1="0" y1="0" x2="0" y2="1">
        <stop offset="0" stop-color="#333333"/>
        <stop offset="1" stop-color="#555555"/>
      </linearGradient>
      <linearGradient id="orangeGrad" x1="0" y1="0" x2="1" y2="1">
        <stop offset="0" stop-color="#e0601a"/>
        <stop offset="1" stop-color="#f0791f"/>
      </linearGradient>
      <linearGradient id="coilGrad" x1="0" y1="0" x2="1" y2="0">
        <stop offset="0" stop-color="#6d737a"/>
        <stop offset="0.5" stop-color="#b9c0c8"/>
        <stop offset="1" stop-color="#8a9099"/>
      </linearGradient>
      <linearGradient id="thermalGrad" x1="0" y1="0" x2="1" y2="0">
        <stop offset="0" stop-color="#4a1f9a"/>
        <stop offset="0.45" stop-color="#e05a2a"/>
        <stop offset="0.75" stop-color="#ffb347"/>
        <stop offset="1" stop-color="#5a2aa0"/>
      </linearGradient>
      <linearGradient id="coalGrad" x1="0" y1="0" x2="0" y2="1">
        <stop offset="0" stop-color="#b9cde0"/>
        <stop offset="0.55" stop-color="#7d7a72"/>
        <stop offset="1" stop-color="#2e2b27"/>
      </linearGradient>
      <linearGradient id="waterGrad" x1="0" y1="0" x2="0" y2="1">
        <stop offset="0" stop-color="#8fb4d6"/>
        <stop offset="0.5" stop-color="#8a8f88"/>
        <stop offset="1" stop-color="#a8a79c"/>
      </linearGradient>
    </defs>

    <rect x="0" y="0" width="1200" height="915" fill="url(#middleGrad)"/>
    <polygon points="812,0 1200,0 1200,448 898,448 868,213" fill="url(#rightGrad)"/>
    <polygon points="0,687 409,687 437,915 0,915" fill="url(#leftGrad)"/>

    <polygon points="0,0 307,0 350,389 0,389" fill="url(#orangeGrad)"/>
    <rect x="0" y="34" width="300" height="30" fill="var(--ink)"/>
    <polygon points="0,389 350,389 363,394 0,394" fill="var(--divider)"/>

    <g role="img" aria-label="Photo of stacked steel coils in a plant">
      <polygon points="307,0 812,0 812,213 330,213" fill="url(#coilGrad)"/>
    </g>

    <polygon points="330,213 850,213 850,241 333,241" fill="var(--band-grey)"/>

    <g role="img" aria-label="Infrared thermal image of electrical cabling">
      <polygon points="0,394 363,394 409,687 0,687" fill="url(#thermalGrad)"/>
    </g>

    <polygon points="0,687 409,687 412,708 0,708" fill="#6e6e6e"/>

    <rect x="898" y="444" width="302" height="4" fill="var(--divider)"/>
    <g role="img" aria-label="Photo of a coal handling stacker at a power plant">
      <polygon points="898,448 1200,448 1200,684 934,684" fill="url(#coalGrad)"/>
    </g>
    <rect x="934" y="684" width="266" height="4" fill="var(--divider)"/>

    <g role="img" aria-label="Photo of digester tanks at a water treatment plant">
      <polygon points="952,688 1200,688 1200,915 985,915" fill="url(#waterGrad)"/>
    </g>
  </svg>

  <h2 class="mission-title">OUR MISSION</h2>
  <div class="block mission-text">
    <p>
      <span class="ln just" style="width:261px">KRT, LLC will provide the highest quality,</span>
      <span class="ln just" style="width:264px">cost effective, world class PdM services in</span>
      <span class="ln just" style="width:267px">the industry. Our commitment to continuing</span>
      <span class="ln just" style="width:270px">education and growth will afford our</span>
      <span class="ln just" style="width:272px">engineers the tools needed to stay on the</span>
      <span class="ln just" style="width:275px">cutting edge of technology. We believe in the</span>
      <span class="ln just" style="width:278px">implementation of Predictive Maintenance</span>
      <span class="ln just" style="width:280px">services to increase overall equipment reliabil-</span>
      <span class="ln just" style="width:283px">ity, reduce costs and improve profitability. Our</span>
      <span class="ln just" style="width:285px">goal is to provide continuous improvements to</span>
      <span class="ln just" style="width:288px">these processes. The company will network with</span>
      <span class="ln just" style="width:292px">various industry professionals to offer the widest</span>
      <span class="ln just" style="width:294px">range of equipment, training and reliability</span>
      <span class="ln just" style="width:297px">services available. Meeting these goals will ensure</span>
      <span class="ln just" style="width:299px">the company’s longevity and allow our valued</span>
      <span class="ln just" style="width:303px">customers to achieve the cost reduction goals that</span>
      <span class="ln">are needed in today’s competitive marketplace.</span>
    </p>
  </div>

  <h2 class="services-title">Services</h2>

  <section class="block" style="left:357px; top:253px;">
    <h3 class="heading">Infrared Thermal Imaging</h3>
    <p>
      <span class="ln" style="margin-left:2px">Infrared thermography is an effective preventative maintenance solution because</span>
      <span class="ln" style="margin-left:4px">it is highly reliable and economically practical. At Kortal Inspection Systems, we</span>
      <span class="ln" style="margin-left:6px">work hand-in hand with plant maintenance departments.</span>
    </p>
  </section>
  <section class="block" style="left:369px; top:333px;">
    <h3 class="heading">Vibration Analysis</h3>
    <p>
      <span class="ln" style="margin-left:3px">Vibration Analysis is the process of monitoring the condition of equipment, and</span>
      <span class="ln" style="margin-left:5px">the diagnosis of faults in equipment through the measurement and analysis of</span>
      <span class="ln" style="margin-left:7px">vibration within that equipment.</span>
    </p>
  </section>
  <section class="block" style="left:383px; top:413px;">
    <h3 class="heading">High Temperature Video &amp; Photography</h3>
    <p>
      <span class="ln" style="margin-left:2px">KRT offers High Temperature Video Inspection as well as custom ambient video and</span>
      <span class="ln" style="margin-left:4px">photographic inspection of your assets.</span>
    </p>
  </section>
  <section class="block" style="left:394px; top:477px;">
    <h3 class="heading">High Speed Video</h3>
    <p>
      <span class="ln" style="margin-left:2px">KRT has the ability to build video components for special application situations.</span>
      <span class="ln" style="margin-left:4px">Some custom build camera and video have been designed for the following appli-</span>
      <span class="ln" style="margin-left:6px">cations Sewer Pipe Inspection, Drain Pipe Inspection, Tank Inspection and Caster</span>
      <span class="ln" style="margin-left:9px">Strand Inspection</span>
    </p>
  </section>
  <section class="block" style="left:409px; top:574px;">
    <h3 class="heading">Laser Alignment</h3>
    <p>
      <span class="ln" style="margin-left:2px">An alignment job that used to take many hours of dial indicating, now takes only a</span>
      <span class="ln" style="margin-left:4px">matter of minutes. Advances in laser alignment equipment and software technology</span>
      <span class="ln" style="margin-left:7px">have made it possible to get pinpoint accuracy in a fraction of the time; saving you</span>
      <span class="ln" style="margin-left:9px">down time and lost production.</span>
    </p>
  </section>
  <section class="block" style="left:425px; top:670px;">
    <h3 class="heading">Dynamic Balancing</h3>
    <p>
      <span class="ln" style="margin-left:3px">High 1X RPM vibration is a good indication of unbalance. High 1X RPM vibration will</span>
      <span class="ln" style="margin-left:6px">also manifest itself as gross misalignment. At KRT we never take it for granted that</span>
      <span class="ln" style="margin-left:8px">other problems such as bad bearings or faulty machine parts can contribute to a high</span>
      <span class="ln" style="margin-left:11px">1X RPM.</span>
    </p>
  </section>
  <section class="block" style="left:441px; top:766px;">
    <h3 class="heading">Motor Meggering</h3>
    <p>
      <span class="ln" style="margin-left:3px">It gives an accurate reading of the measure of resistance and continuity available in a</span>
      <span class="ln" style="margin-left:5px">high-voltage circuit and electrical motor. Using the Ohmtrak to test a three-phase motor</span>
      <span class="ln" style="margin-left:8px">is rather easy, though the safety hazards for this procedure are quite high. Be sure to</span>
      <span class="ln" style="margin-left:10px">follow good safety measures to prevent electrical shock. This is important, because the</span>
      <span class="ln" style="margin-left:13px">high-voltage current in three-phase systems is far more lethal than a mere low-voltage</span>
      <span class="ln" style="margin-left:15px">shock received in residential setting.</span>
    </p>
  </section>

  <section class="block" style="left:817px; top:21px;">
    <h3 class="heading">Ultrasonic Thickness Testing</h3>
    <p style="margin-top:17px">
      <span class="ln just" style="margin-left:6px; width:352px">Using Halvern and Stenrock instruments, KRT can test</span>
      <span class="ln just" style="margin-left:11px; width:347px">vessel wall thickness, tank thickness, and piping thickness.</span>
      <span class="ln just" style="margin-left:14px; width:344px">A detailed comprehensive report can provide you with</span>
      <span class="ln just" style="margin-left:17px; width:341px">much needed information like the following: Metal Loss,</span>
      <span class="ln just" style="margin-left:20px; width:338px">Corrosion Rate, Percentage of Allowable Wall Loss,</span>
      <span class="ln just" style="margin-left:25px; width:333px">Estimated Remaining Tank or Pressure Vessel Life,</span>
      <span class="ln" style="margin-left:27px">Estimated Retirement Date, Overall Tank Condition.</span>
    </p>
  </section>
  <section class="block" style="left:855px; top:198px;">
    <h3 class="heading">Oil Analysis</h3>
    <p style="margin-top:16px">
      <span class="ln just" style="margin-left:7px; width:313px">Oil Analysis is an excellent Predictive Maintenance</span>
      <span class="ln" style="margin-left:11px">Technology offered by KRT, LLC.</span>
      <span class="ln" style="height:16px"></span>
      <span class="ln just" style="margin-left:17px; width:303px">KRT utilizes the newest technologies of lubricant</span>
      <span class="ln just" style="margin-left:21px; width:299px">analysis to support your Predictive Maintenance</span>
      <span class="ln just" style="margin-left:25px; width:295px">Program. We use a full-service off-site Tribology</span>
      <span class="ln just" style="margin-left:28px; width:292px">lab to perform the most comprehensive testing of</span>
      <span class="ln just" style="margin-left:31px; width:289px">in-service lubricants to provide associated Wear</span>
      <span class="ln" style="margin-left:35px">Debris Analysis for true condition monitoring.</span>
      <span class="ln just" style="margin-left:39px; width:281px">All it takes is a routine 4-ounce sample of oil</span>
      <span class="ln just" style="margin-left:42px; width:278px">from your plant machinery. Lubricant Analysis</span>
      <span class="ln just" style="margin-left:46px; width:274px">Programs provide “Solutions That Keep You</span>
      <span class="ln" style="margin-left:50px">Running”</span>
    </p>
  </section>

  <h3 class="list-title">List Of Services We Offer:</h3>
  <ul class="service-list">
    <li>Infrared Thermal Imaging</li>
    <li>Vibration Analysis</li>
    <li>High Temperature Video &amp; Photography</li>
    <li>High Speed Video</li>
    <li>Laser Alignment</li>
    <li>Dynamic Balancing</li>
    <li>Motor Meggering</li>
    <li>Leak Detection</li>
    <li>Ultrasonic Thickness Testing</li>
    <li>Oil Analysis</li>
  </ul>
</main>
</body>
</html>
```